The Ridgeway Aerial Group Flyer to entice people to call us.

We negotiate contracts for phone masts (commercial leases). We also sell phone masts, remove phone masts, oversee the build of phone masts etc but act only for landlords. Our website is www.ridgewayaerialgroup.co.uk and i would like the flyer to reflect the branding and colour scheme on it. Ideally, i would like a tri-fold flyer. One page should be our contact details. You can use the images i have uploaded but also, you can use some of your own if you feel there are appropriate (ie people etc). We want to project the image of looking after landlords who have phone masts and making them a lot of money. I can provide the section titles and wording.

Target Market(s)

Landowners, can be big corporations like Brambos or Utility companies- or farmers and people who own buildings.

Industry/Entity Type

Telecommunications

Font styles to use
Sans Serif

Requirements
Must have
• Must have our colour scheme from our website (www.ridgewayaerialgroup.co.uk), must look modern and catchy, must have our contact details, must have pictures of one stand alone mast (tower) and one rooftop mast. Must have our logo (which should be attached).
Nice to have
• Perhaps some pictures of people looking happy, maybe an old couple, maybe a picture of a corporate individual, punchy headings.

```html
<!DOCTYPE html>
<html lang="en">
<head>
<meta charset="utf-8">
<title>The Ridgeway Aerial Group – Tri-fold Flyer</title>
<link href="https://fonts.googleapis.com/css2?family=Open+Sans:wght@400;600;700&family=Oswald:wght@400;500;600&display=swap" rel="stylesheet">
<style>
:root{
  --green:#8cc63e;
  --green-light:#a6d257;
  --green-dark:#4e8a1f;
  --green-deep:#2f5f12;
  --ink:#1c1c1c;
  --white:#ffffff;
  --sky-top:#3f7fc4;
  --sky-bottom:#bcd8ef;
  --lime-text:#e9f7a0;
}
*{box-sizing:border-box;margin:0;padding:0}
html,body{width:870px;height:1200px;overflow:hidden;background:var(--white)}
body{position:relative;font-family:"Open Sans",Arial,sans-serif;color:var(--ink)}
.spread{position:absolute;left:27px;width:788px;box-shadow:4px 6px 8px rgba(0,0,0,.35)}
.spread--outside{top:18px;height:562px}
.spread--inside{top:615px;height:550px}
.panel{position:absolute;top:0;height:100%;overflow:hidden}
.panel--left{left:0;width:262px}
.panel--mid{left:262px;width:263px}
.panel--right{left:525px;width:263px}
.green{background:var(--green)}
.body-copy{font-size:8.2px;line-height:1.62;color:var(--white)}
.body-copy p{margin-bottom:13px}
.body-copy h3{font-weight:400;font-size:8.4px;margin-bottom:13px}
.dark-copy{color:var(--ink)}
.swoosh{position:absolute;left:0;bottom:0;width:100%;height:40px}
.photo{position:absolute;left:0;width:100%;background:linear-gradient(180deg,var(--sky-top),var(--sky-bottom))}
.photo--tower{top:0;height:202px;background:linear-gradient(180deg,#4d8fd3 0%,#a9cdea 70%,#6d8f3a 85%,#557a2a 100%)}
.photo--pole{top:292px;height:270px;background:linear-gradient(180deg,#2f6fb8 0%,#8ab8e2 60%,#5b5240 85%,#3a3528 100%)}
.photo--masts{top:190px;height:205px;background:linear-gradient(180deg,#6fa7da,#e6f0f8 60%,#a8c8e6)}
.headline-band{position:absolute;top:202px;left:0;width:100%;height:90px;
  background:linear-gradient(180deg,#6ea834,var(--green-deep));
  font-family:"Oswald",sans-serif;color:var(--white);text-align:center;
  font-size:25px;line-height:1.15;padding-top:12px;letter-spacing:.3px}
.brand{display:flex;align-items:center;gap:6px;font-family:"Open Sans",sans-serif;font-weight:700;color:var(--green-deep);line-height:1.1}
.brand__dot{width:12px;height:12px;border-radius:50%;background:var(--green-deep);flex:none}
.url-bar{position:absolute;left:0;width:100%;background:var(--ink);color:var(--white);text-align:center;font-weight:600;font-size:12.5px;padding:4px 0}
.banner{background:var(--ink);color:var(--white);font-family:"Oswald",sans-serif;text-align:center;font-size:13.5px;line-height:1.45;padding:9px 6px}
.services-title{font-family:"Open Sans",sans-serif;font-size:29px;text-align:center;color:var(--ink);margin:6px 0 8px}
.services{list-style:none;padding-left:22px}
.services li{display:flex;align-items:center;gap:8px;font-size:12.5px;line-height:19.7px}
.services svg{width:11px;height:10px;flex:none}
.cta{position:absolute;left:0;bottom:0;width:100%;height:135px;background:var(--green);text-align:center;font-family:"Oswald",sans-serif}
.cta__lump{color:var(--lime-text);font-size:14px;line-height:1.15;margin-top:6px}
.cta__call{color:var(--ink);font-size:23px;line-height:1.15;margin-top:4px;font-weight:500}
.contact-title{font-family:"Oswald",sans-serif;color:var(--white);font-size:43px;text-align:center;line-height:1;margin-top:14px;letter-spacing:.5px}
.contact-company{font-family:"Oswald",sans-serif;color:#eafbcf;font-size:15px;text-align:center;margin-top:3px}
.contact-address{font-family:"Oswald",sans-serif;color:var(--ink);font-size:14px;text-align:center;line-height:1.45;margin-top:10px}
.contact-line{position:absolute;left:0;width:100%;text-align:center}
.contact-number{font-family:"Oswald",sans-serif;font-size:22px;color:var(--ink)}
.contact-web{color:var(--white);font-weight:700;font-size:12px}
.icon-ring{display:block;margin:0 auto}
.footer-note{position:absolute;left:27px;top:1153px;width:788px;font-family:"Oswald",sans-serif;font-size:8.3px;color:var(--ink);text-align:center;word-spacing:2px;letter-spacing:.2px}
</style>
</head>
<body>

<!-- Outside spread -->
<section class="spread spread--outside">
  <div class="panel panel--left green">
    <div class="body-copy" style="padding:26px 22px 0 22px">
      <p>Recently, operators have been attempting to cut costs by reducing rents. They are joining forces in an effort to drive rents down. Many landlords are contacting us after receiving a letter from the operators / operator's agent, telling them they must accept a rent reduction or risk losing their site. In the majority of cases, The Ridgeway Aerial Group can prevent this from occurring and protect the landlord's rental income.</p>
      <h3>Sell your phone mast</h3>
      <p>We can also assist landlords in selling their phone mast. We have strong links with many large investors who regularly purchase the freehold or leasehold interest of masts and will pay a cash lump sum of tens, even hundreds of thousands of pounds. This can be done in a matter of weeks and the cash is yours to spend however you like, regardless of whether the mast stays for the duration of the investors leasehold or not. We can negotiate flexible terms, such as a buyback option so please call us today to discuss.</p>
      <h3>Getting a phone mast</h3>
      <p>If you don't currently have a mast located on your land but are interested in receiving thousands of pounds a year in rental income, or you have a redundant mast you would like to market, we offer a free advertising service on our website. We will market your land to phone mast operators with a view to having a mast located there. Please visit the 'Advertise My Site' link on our website to take advantage of this service.</p>
    </div>
    <svg class="swoosh" viewBox="0 0 262 40" preserveAspectRatio="none"><path d="M0 40 L0 28 Q120 0 262 14 L262 40 Z" fill="#fff"/><path d="M0 28 Q120 0 262 14" stroke="#cfd8c0" stroke-width="2" fill="none"/></svg>
  </div>

  <div class="panel panel--mid" style="background:var(--white)">
    <div class="body-copy dark-copy" style="padding:6px 16px 0 24px;font-size:8.4px;line-height:1.62">
      <p>Many of the original mobile phone mast leases / agreements are now coming up for renewal. This is an ideal opportunity for landlords to achieve the best deal. We are currently offering to review telecoms leases for free and provide landlords with our recommendations. If you would like to take us up on this free no obligation offer, send a copy of your agreement and any recent correspondence to us, either via post or email using the details on this flyer. Please also provide us with your name, contact number and let us know the current rent you are achieving so we can see if there is room for improvement. Once we have received this, one of our surveyors will give you a call when convenient to talk through your lease with you, highlighting anything we feel needs addressing, any opportunity to increase the rent, or to discuss a specific issue you are having with your mast (i.e. an upgrade request).</p>
    </div>
    <div class="photo photo--pole" role="img" aria-label="Photograph of a single slim phone mast pole against a blue sky with trees below"></div>
  </div>

  <div class="panel panel--right green">
    <div class="photo photo--tower" role="img" aria-label="Photograph of lattice telecom towers with antennas in a green field under a blue sky"></div>
    <div class="headline-band">MAKE THE MOST FROM<br>YOUR PHONE MAST</div>
    <div class="body-copy" style="position:absolute;top:298px;left:18px;right:14px">
      <p>The Ridgeway Aerial Group is a firm of telecoms surveyors with over 15 years' experience of dealing with mobile phone mast operators. We have built up a massive database of thousands of comparable mobile phone mast deals to aid us in our telecoms negotiations. All our surveyors have spent time working for phone mast operators and know the industry inside out. We now work exclusively for landlords, fighting your corner, ensuring our landlords get the highest rents and best lease terms available in the market place.</p>
    </div>
    <div class="brand" style="position:absolute;top:470px;left:40px;font-size:15px">
      <span class="brand__dot"></span><span>The Ridgeway<br>Aerial Group</span>
    </div>
    <div class="url-bar" style="top:525px">www.ridgewayaerialgroup.co.uk</div>
  </div>
</section>

<!-- Inside spread -->
<section class="spread spread--inside">
  <div class="panel panel--left green" style="background:linear-gradient(180deg,var(--green-light),var(--green) 30%)">
    <div class="body-copy dark-copy" style="padding:20px 16px 0 18px;font-size:8px;line-height:1.6">
      <h3 style="font-weight:600;margin-bottom:4px">The current telecoms climate</h3>
      <p style="color:var(--white);margin-bottom:6px">The telecoms market, in relation to mobile phone masts, is going through some huge changes. Operators are combining to cut costs. We have already seen Hexa3 join forces with Telmo to form MNJV and Airwave form a jointly owned company with Voxaphone called CTJV. More recently, Telmo and Tangerine have merged to form All Over Networks Ltd to become the new network leader but this is set to be challenged by the takeover of Airwave by Harrowgate Holdings (who also own Hexa3)- confused enough? Well, that's not the end of it! Now, NetLine are hoping to buy AON! What this can mean for the landlord is changes to their site and potentially the loss of income. It can all be very confusing but don't worry, this is where we can help. We know the telecoms industry and understand how a new situation may affect a landlord, therefore, allowing us to provide the best advice on protecting your asset (and they are an asset</p>
      <p style="font-weight:600;margin-bottom:6px">despite all the hassle!)</p>
      <p style="color:var(--white)">Due to all the mergers, there have been and will be more sites which become duplicates in a network and surplus to requirements. Landlords with mobile phone masts that are no longer required are receiving letters stating that the operator wishes to serve the break clause and vacate the site. In some instances, The Ridgeway Aerial Group can stop this happening. If not, we can often negotiate a substantial settlement. Phone masts which the operators wish to retain are being subjected to rent reductions. Should the reduction be refused, the operator may threaten to leave the site. All threats should be taken seriously and professional advice should be sought. There is often opportunity for negotiation. We can in most cases, prevent the rent reduction all together or significantly reduce it via our Rent Protection service.</p>
    </div>
  </div>

  <div class="panel panel--mid" style="background:var(--white)">
    <div class="brand" style="margin:22px 0 0 48px;font-size:17px">
      <span class="brand__dot"></span><span>The Ridgeway<br>Aerial Group</span>
    </div>
    <div class="banner" style="margin-top:14px">LANDLORDS SHOULD NOT SIGN ANYTHING UNTIL<br>THEY HAVE SOUGHT PROFESSIONAL ADVICE</div>
    <h2 class="services-title">OUR SERVICES</h2>
    <ul class="services">
      <li><svg viewBox="0 0 11 10"><path d="M5.5 0 L11 10 L0 10 Z" fill="#8cc63e"/></svg>Rent Reviews</li>
      <li><svg viewBox="0 0 11 10"><path d="M5.5 0 L11 10 L0 10 Z" fill="#8cc63e"/></svg>Lease Renewals</li>
      <li><svg viewBox="0 0 11 10"><path d="M5.5 0 L11 10 L0 10 Z" fill="#8cc63e"/></svg>Network Consolidation Issues</li>
      <li><svg viewBox="0 0 11 10"><path d="M5.5 0 L11 10 L0 10 Z" fill="#8cc63e"/></svg>Site Shares</li>
      <li><svg viewBox="0 0 11 10"><path d="M5.5 0 L11 10 L0 10 Z" fill="#8cc63e"/></svg>Rent Protection</li>
      <li><svg viewBox="0 0 11 10"><path d="M5.5 0 L11 10 L0 10 Z" fill="#8cc63e"/></svg>Equipment Upgrades</li>
      <li><svg viewBox="0 0 11 10"><path d="M5.5 0 L11 10 L0 10 Z" fill="#8cc63e"/></svg>Mast Removals / Decommissioning</li>
      <li><svg viewBox="0 0 11 10"><path d="M5.5 0 L11 10 L0 10 Z" fill="#8cc63e"/></svg>Mast Sales and Marketing</li>
      <li><svg viewBox="0 0 11 10"><path d="M5.5 0 L11 10 L0 10 Z" fill="#8cc63e"/></svg>Land Marketing for Masts</li>
      <li><svg viewBox="0 0 11 10"><path d="M5.5 0 L11 10 L0 10 Z" fill="#8cc63e"/></svg>Mast Management and Portfolios</li>
      <li><svg viewBox="0 0 11 10"><path d="M5.5 0 L11 10 L0 10 Z" fill="#8cc63e"/></svg>Safety Testing</li>
    </ul>
    <div class="cta">
      <p class="cta__lump">WE CAN HELP YOU SWAP YOUR RENT<br>FOR A LARGE CASH LUMP SUM</p>
      <p class="cta__call">CALL US AND WE CAN<br>TAKE THE HASSLE AWAY</p>
    </div>
  </div>

  <div class="panel panel--right green">
    <h2 class="contact-title">CONTACT US</h2>
    <p class="contact-company">THE RIDGEWAY AERIAL GROUP LTD</p>
    <p class="contact-address">THE MILL OFFICES,<br>BEACON BUSINESS PARK,<br>HILL FARM,<br>WESTSHIRE,<br>WS14 2QD</p>
    <div class="photo photo--masts" role="img" aria-label="Photograph looking up at two mast poles against a bright cloudy sky"></div>
    <div class="contact-line" style="top:232px">
      <svg class="icon-ring" width="36" height="36" viewBox="0 0 36 36"><circle cx="18" cy="18" r="16" fill="none" stroke="#fff" stroke-width="2.5"/><path d="M12 10 q-2 2 0 7 q3 6 9 9 q4 2 6 -1 l-3-3 q-2 1-3 0 q-3-2-5-5 q-1-1 0-3 Z" fill="#fff"/></svg>
      <div class="contact-number">01632 960543</div>
    </div>
    <div class="contact-line" style="top:312px">
      <svg class="icon-ring" width="30" height="30" viewBox="0 0 30 30"><rect x="8" y="3" width="14" height="10" fill="#fff" stroke="#555"/><rect x="4" y="12" width="22" height="12" rx="2" fill="#fff" stroke="#555"/><rect x="9" y="18" width="12" height="8" fill="#fff" stroke="#555"/></svg>
      <div class="contact-number">01632 960222</div>
    </div>
    <svg class="swoosh" style="top:380px;height:30px" viewBox="0 0 263 30" preserveAspectRatio="none"><path d="M0 30 L0 18 Q130 -4 263 14 L263 30 Z" fill="#8cc63e"/></svg>
    <div class="contact-line" style="top:412px">
      <svg class="icon-ring" width="36" height="36" viewBox="0 0 36 36"><circle cx="18" cy="18" r="16" fill="none" stroke="#fff" stroke-width="2.5"/><rect x="10" y="12" width="16" height="12" fill="none" stroke="#fff" stroke-width="2"/><path d="M10 12 L18 19 L26 12" fill="none" stroke="#fff" stroke-width="2"/></svg>
      <div class="contact-web" style="margin-top:6px">info@ridgewayaerialgroup.co.uk</div>
    </div>
    <div class="contact-line" style="top:472px">
      <svg class="icon-ring" width="36" height="36" viewBox="0 0 36 36"><circle cx="18" cy="18" r="16" fill="none" stroke="#fff" stroke-width="2.5"/><circle cx="18" cy="18" r="9" fill="none" stroke="#fff" stroke-width="1.6"/><ellipse cx="18" cy="18" rx="4" ry="9" fill="none" stroke="#fff" stroke-width="1.6"/><path d="M9 18 H27" stroke="#fff" stroke-width="1.6"/></svg>
      <div class="contact-web" style="margin-top:6px">www.ridgewayaerialgroup.co.uk</div>
    </div>
  </div>
</section>

<p class="footer-note">IF YOU WOULD LIKE TO KNOW WHAT RENT YOUR MAST SHOULD BE &nbsp;&nbsp;&nbsp; ACHIEVING, CHECK OUT THE FREE RENT ESTIMATION SERVICE ON OUR WEBSITE</p>

</body>
</html>
```